Company Business Cards Based on Existing Design Scheme

We are looking for 9cmx5cm business cards (standard rectangular shape, no cutouts) that are fresh, clean and modern and fit with the design of our current website, brightwave.com.au. See "Must Haves" for requirements.

Please include the PSD files so we can modify for new staff members.

Although this project is due to close on Saturday, we would like the design as soon as possible, so designers who submit early will be prioritised.

Thanks! Looking forward to your designs!

Industry/Entity Type

Business

Contact Information for Business Card

9cm by 5cm, standard rectangular shape, no cutouts or strange shapes

Font styles to use
Sans Serif

Requirements
Must have
• Company logo (attached) can go on front or back (may be changed to white text with grey icon, white text with white icon, or remain as teal text with grey icon)
• May also use our icon (the two side-by-side figures, attached, can be changed to white or teal) anywhere throughout the design
• Colours (use any of the following):
• - Dark teal: CMYK 84,26,45,3 (hex #008d8e)
• - Orange (use sparingly): 0,47,100,0 (#ff9a00)
• - Light teal: 49,4,24,0 (#7fc6c6)
• - Grey: 0,2,0,26 (#717074)
• Fonts: Gotham Light, Helvetica, or similar
• FRONT:
• Name (e.g. marnie holtby)
• Title (e.g. digital marketing & communications specialist)
• Address (level 4, 187 wattle street sydney nsw 2000)
• Phone (1300 584 906)
• Mobile phone (e.g. 0492 718 340)
• Email address (e.g. name@brightwave.com.au)
• Website address (brightwave.com.au)
• Twitter icon with handle (e.g. @bwvMarnie)
• LinkedIn icon with address (e.g. proflink.net/in/marnieh)
• BACK:
• The text "skilled people, placed quickly."
• Social icons with URLs:
• - Twitter icon with @brightwave
• - LinkedIn icon with linkd.in/bwvstaffing and linkd.in/bwvnetwork
• - Facebook icon with facebook.com/brightwavestaffing
• - Google+ icon with google.com/+brightwaveOceania
• - YouTube icon with youtube.com/bwvharbour
• - RSS icon with brightwave.com.au/blog

```html
<!DOCTYPE html>
<html lang="en">
<head>
<meta charset="utf-8">
<title>brightwave business card</title>
<link href="https://fonts.googleapis.com/css2?family=Questrial&display=swap" rel="stylesheet">
<style>
  :root {
    --teal: #109fab;
    --grey: #6d6e71;
    --white: #ffffff;
    --backdrop: #e6e7e8;
  }
  * { box-sizing: border-box; margin: 0; padding: 0; }
  html, body { width: 1200px; height: 1000px; overflow: hidden; }
  body {
    background: var(--backdrop);
    font-family: "Questrial", "Century Gothic", sans-serif;
    position: relative;
  }
  .card {
    position: absolute;
    left: 265px;
    width: 666px;
    height: 397px;
    overflow: hidden;
    box-shadow: 0 2px 6px rgba(0,0,0,0.18);
  }
  .card--front { top: 73px; background: var(--white); }
  .card--back { top: 532px; background: var(--teal); color: var(--white); }

  /* front */
  .logo-band {
    position: absolute;
    left: 0; top: 169px;
    width: 332px; height: 59px;
    background: var(--teal);
    display: flex; align-items: center; justify-content: flex-end;
    padding-right: 14px;
  }
  .wordmark { color: var(--white); font-size: 40px; letter-spacing: 0.5px; line-height: 1; }
  .person { position: absolute; left: 354px; top: 61px; }
  .person__name { color: var(--teal); font-size: 27px; line-height: 30px; font-weight: 400; }
  .person__title { color: var(--grey); font-size: 17px; line-height: 20px; }
  .address {
    position: absolute; left: 354px; top: 180px;
    color: var(--grey); font-size: 17px; line-height: 20px; font-style: normal;
  }
  .contact-list {
    position: absolute; left: 354px; top: 236px;
    list-style: none; color: var(--grey); font-size: 17px;
  }
  .contact-list li { display: flex; align-items: center; height: 19.6px; }
  .contact-list svg { width: 14px; height: 14px; margin-right: 7px; fill: var(--teal); flex: none; }

  /* back */
  .back-logo {
    position: absolute; left: 0; right: 0; top: 52px;
    text-align: center; font-size: 46px; line-height: 1;
  }
  .tagline {
    position: absolute; left: 0; right: 0; top: 160px;
    text-align: center; font-size: 17px;
  }
  .social {
    position: absolute;
    transform: translateX(-50%);
    display: flex; flex-direction: column; align-items: center;
    font-size: 15px; white-space: nowrap;
  }
  .social__dot {
    width: 11px; height: 11px; border-radius: 50%;
    background: var(--white); margin-bottom: 13px;
  }
</style>
</head>
<body>

<section class="card card--front" aria-label="card front">
  <div class="logo-band"><span class="wordmark">brightwave</span></div>

  <div class="person">
    <h1 class="person__name">marnie holtby</h1>
    <p class="person__title">Managing Director</p>
  </div>

  <address class="address">
    level 4, 187 wattle street<br>
    sydney nsw 2000
  </address>

  <ul class="contact-list">
    <li><svg viewBox="0 0 14 14" aria-hidden="true"><path d="M1 3h12v8H1z M1.5 3.5 7 8l5.5-4.5" fill="none" stroke="#109fab" stroke-width="1.4"/></svg>info@brightwave.com.au</li>
    <li><svg viewBox="0 0 14 14" aria-hidden="true"><circle cx="7" cy="7" r="5"/></svg>@bwvMarnie</li>
    <li><svg viewBox="0 0 14 14" aria-hidden="true"><circle cx="7" cy="7" r="5"/></svg>proflink.net/in/marnieh</li>
    <li><svg viewBox="0 0 14 14" aria-hidden="true"><rect x="4" y="1" width="6" height="12" rx="1" fill="none" stroke="#109fab" stroke-width="1.3"/></svg>999 999 9999</li>
    <li><svg viewBox="0 0 14 14" aria-hidden="true"><path d="M2 5c0-2 10-2 10 0v1H9.5V4.5h-5V6H2z M3.5 7h7l1.5 5H2z"/></svg>999 999 9999</li>
    <li><svg viewBox="0 0 14 14" aria-hidden="true"><circle cx="7" cy="7" r="5.5" fill="none" stroke="#109fab" stroke-width="1.2"/><path d="M1.5 7h11M7 1.5v11M7 1.5c-3 3-3 8 0 11M7 1.5c3 3 3 8 0 11" fill="none" stroke="#109fab" stroke-width="1"/></svg>brightwave.com.au</li>
  </ul>
</section>

<section class="card card--back" aria-label="card back">
  <div class="back-logo">brightwave</div>
  <p class="tagline">skilled people, placed quickly.</p>

  <div class="social" style="left:80px; top:250px;"><span class="social__dot"></span>@bwvMarnie</div>
  <div class="social" style="left:332px; top:250px;"><span class="social__dot"></span>bwvstaffing / bwvnetwork</div>
  <div class="social" style="left:585px; top:250px;"><span class="social__dot"></span>bwvharbour</div>
  <div class="social" style="left:167px; top:312px;"><span class="social__dot"></span>brightwavestaffing</div>
  <div class="social" style="left:497px; top:312px;"><span class="social__dot"></span>brightwaveOceania</div>
</section>

</body>
</html>
```